依頼詳細
【サイトマップ】
TOPページ
---HOME
---COMPANY (会社概要/会社沿革)
---BUSINESS (事業内容)
---RECRUIT  (採用情報)
---CONTACT  (問い合わせ)
---NEWS  (新着情報)
【サイト作成においてのポイント】
・レスポンシブデザインでお願いいたします。
・各所の素材は全てURLをお送り下さい。

【イメージ全体配置構図(いれていただきたい要素)】

ワイヤーフレームをご確認ください。
①~⑧までワイヤーフレーム内にふった番号順に詳細を記載しております。

※ワイヤーフレームはあくまでも入れたい要素を並べた一例になります。
各配置、表示位置は変えていただいても問題ございません。
------------------------

①グローバルナビ
配置は上部でお願いいたします。位置は中央を希望いたします。
------

②メインビジュアル
メインビジュアルは動画(アニメーション)挿入の仕様想定で作成して頂きたいです。
参考サイト:http://www.kelvora-sample.com/
http://updates.pimaru-breeze.jp/

1ページまるごと動画(アニメーション)仕様でも問題ございません。
参考サイト:http://www.tosquivel.com/

(こちらでは素材を用意しておりません。確認後、購入手続きをさせていただきますのでURLをお送りください)
サイズはどのデバイスでも横幅が100%になるように考えております。
縦幅はお任せしますので、素材にあわせていただけますと幸いです。
------

③新着情報
新着情報は3つ以上いれていただけますと幸いです
いれていただきたい要素は
・更新日時(年,月,日)
・更新内容のテキスト部分 20文字前後

各テキストの配置箇所、文字色、フォント、文字やボタンのサイズ、幅感等の指定はございません。
ワイヤーフレームにはいれていただきたい要素だけならべています。
------

④事業紹介箇所
入れていただきたい要素は以下になります。
・事業紹介イメージ素材
メイン動画がヘッダー部分のみに表示の場合
背景画像として、サイズは横が100%になるように考えております。
メイン動画が全体の場合
イメージ素材が浮き上がってくるようなアニメーション仕様で考えておりますので、その仕様にあったサイズ、表示方法にしていただけますと幸いです。

極力どのデバイスサイズでもバランスよく見えるような素材をご使用いただけますと幸いです。

・事業内容の名前
(Internet media、Promotion、Influencer Marketing)
・以下テキスト
(KanoMireaはインターネットを軸とした事業を展開しております。)
・下層ページへのリンクボタン

------

⑤入れていただきたい要素は以下になります。
・背景素材
メイン動画がヘッダー部分のみに表示の場合
メイン動画が全体の場合

・遷移先の中に含まれる内容の紹介
(Staff Interview、One Day、Blog)
・以下テキスト
(KanoMireaの福利厚生や、メンバーの1日の勤務スケジュールを公開)
・下層ページへのリンクボタン

------

⑥入れていただきたい要素は以下になります。
・背景素材
メイン動画がヘッダー部分のみに表示の場合
メイン動画が全体の場合

・遷移先の中に含まれる内容の紹介
(overview/ history、Greeting)
・以下テキスト
(会社概要・沿革・代表挨拶)
・下層ページへのリンクボタン

------

⑦フッター
サイト案内
------

⑧会社情報、ロゴ

以上になります。

ご不明点等がございましたらお気軽にお問い合わせ下さい。
何卒よろしくお願い申し上げます。
ページ数
1ページ
希望イメージ
• +5 0 +5
• シンプル
複雑
• 単色
カラフル
• 暗い
明るい
• 日常
高級
• 遊び心
厳粛
• 未来的
伝統的
• 女性的
男性的
希望する色
青系、水色系、グレー系、紫系
納品ファイル
• フォトショップ形式 (.psd)
補足説明
SD又は、FireworksPNGデータ
動画に関しましてはデータ添付またはURLをお送りいただけますと幸いです。
依頼公開後の追記内容
もう少し様々な作品を拝見させていただきたく、延長させていただきました。
引き続き、何卒よろしくお願いいたします。
■ 選んだ理由

全体の雰囲気が1番理想とするものに近く、構図も綺麗なバランスで組み立てられていました。
コーポレートサイトとしてシンプルかつおしゃれ見やすいものに仕上がると思い、rusofu様の作品を選ばせていただきました。

■ 提案者全員のお礼・コメント

各ランサー様
この度は弊社へのコンペへご参加いただき、誠にありがとうございました。
どの作品も大変素晴らしく、当選させていただきたいアイディア、デザインがたくさんありました。
また機会がございましたら、作品をご投稿下さいますと幸いに存じます。
誠にありがとうございました。

```html
<!DOCTYPE html>
<html lang="ja">
<head>
<meta charset="utf-8">
<title>Kano Mirea</title>
<link rel="stylesheet" href="https://fonts.googleapis.com/css2?family=Lato:ital,wght@0,400;0,700;0,900;1,700;1,900&family=Noto+Sans+JP:wght@400;500;700&display=swap">
<style>
:root{
  --white:#ffffff;
  --ink:#333a44;
  --muted:#8a9099;
  --line:#e3e5e8;
  --blue:#2f5ed6;
  --navy:#0f2b4c;
  --navy-deep:#0a1f38;
  --footer-text:#b9c6d6;
}
*{margin:0;padding:0;box-sizing:border-box}
html,body{width:1200px;height:3424px;overflow:hidden}
body{font-family:"Noto Sans JP","Lato",sans-serif;color:var(--ink);background:var(--white)}
.section{position:relative;width:1200px;overflow:hidden}
.photo{position:absolute;inset:0}

/* hero */
.hero{height:660px}
.hero .photo{background:linear-gradient(180deg,#b9c1c8 0%,#9aa4ad 45%,#6f747a 100%)}
.hero .shade{position:absolute;inset:0;background:linear-gradient(180deg,rgba(0,0,0,.15),rgba(0,0,0,.05) 40%,rgba(0,0,0,.2))}
.brand{position:absolute;top:40px;left:0;width:100%;display:flex;justify-content:center;align-items:center;gap:10px;color:var(--white);font-family:"Lato",sans-serif;font-weight:700;font-size:26px;letter-spacing:.5px}
.brand .dot{width:24px;height:24px;border-radius:50%;background:var(--white)}
.gnav{position:absolute;top:118px;left:0;width:100%;display:flex;justify-content:center;gap:30px}
.gnav a{color:var(--white);text-decoration:none;font-family:"Lato",sans-serif;font-size:15px;letter-spacing:1px;padding-bottom:6px}
.gnav a.current{border-bottom:2px solid var(--white)}
.hero-title{position:absolute;top:280px;left:0;width:100%;text-align:center;color:var(--white);font-family:"Lato",sans-serif;font-style:italic;font-weight:900;font-size:118px;letter-spacing:1px;text-shadow:0 2px 12px rgba(0,0,0,.25)}

/* news */
.news{height:540px;background:var(--white)}
.section-label{position:absolute;top:720px;left:0}
.news-label{position:absolute;top:58px;left:0;width:100%;text-align:center;font-family:"Lato",sans-serif;font-size:17px;letter-spacing:3px;color:var(--ink)}
.news-label::after{content:"";display:block;width:40px;height:2px;background:var(--ink);margin:10px auto 0}
.news-list{position:absolute;top:132px;left:32px;display:flex;gap:28px}
.news-card{width:264px;height:320px;background:var(--white);box-shadow:0 2px 10px rgba(0,0,0,.12)}
.news-card .thumb{height:160px;background:linear-gradient(135deg,#8f8a86,#c7b9ae 60%,#7c7470)}
.news-body{padding:16px 18px}
.news-date{font-family:"Lato",sans-serif;font-size:12px;color:var(--muted)}
.news-text{margin-top:8px;font-size:13px;line-height:1.7;color:var(--ink)}
.news-more{margin-top:18px;padding-top:12px;border-top:1px solid var(--line);display:flex;justify-content:space-between;font-family:"Lato",sans-serif;font-size:11px;letter-spacing:1px;color:var(--ink)}

/* feature blocks */
.feature{height:580px}
.feature .shade{position:absolute;inset:0}
.business .photo{background:linear-gradient(120deg,#1b2a40 0%,#34465e 45%,#5d6d80 75%,#2b3648 100%)}
.business .shade{background:linear-gradient(90deg,rgba(10,20,40,.55),rgba(10,20,40,.1))}
.recruit .photo{background:linear-gradient(110deg,#6f6a66 0%,#a79d94 35%,#55514f 65%,#2f3134 100%)}
.recruit .shade{background:linear-gradient(270deg,rgba(0,0,0,.45),rgba(0,0,0,0) 60%)}
.company .photo{background:linear-gradient(100deg,#7a6a58 0%,#3b3b3e 35%,#24272c 55%,#8d9298 80%,#c9cdd1 100%)}
.company .shade{background:linear-gradient(90deg,rgba(0,0,0,.4),rgba(0,0,0,0) 55%)}
.feature-copy{position:absolute;color:var(--white)}
.feature-title{font-family:"Lato",sans-serif;font-style:italic;font-weight:900;font-size:60px;letter-spacing:8px;line-height:1}
.feature-lead{margin-top:16px;font-size:15px;letter-spacing:1px;line-height:1.6}
.feature-items{margin-top:22px;list-style:none;font-family:"Lato",sans-serif;font-style:italic;font-weight:900;font-size:20px;letter-spacing:2px;line-height:44px}
.btn{display:inline-flex;align-items:center;justify-content:center;gap:8px;margin-top:30px;width:196px;height:34px;background:var(--blue);color:var(--white);font-family:"Lato",sans-serif;font-size:12px;letter-spacing:1px;text-decoration:none}
.business .feature-copy{top:130px;left:124px}
.recruit .feature-copy{top:162px;left:680px}
.company .feature-copy{top:120px;left:124px}

/* footer */
.site-map{height:240px;background:var(--navy)}
.site-map-cols{position:absolute;top:48px;left:120px;display:flex;gap:0}
.site-map-col{width:200px}
.site-map-col h3{font-family:"Lato",sans-serif;font-weight:400;font-size:12px;color:var(--white);padding-bottom:8px;border-bottom:1px solid rgba(255,255,255,.3);margin-right:40px}
.site-map-col ul{list-style:none;margin-top:12px}
.site-map-col li{font-size:11px;color:var(--footer-text);line-height:28px}
.site-map-col li::before{content:"›";margin-right:8px}
.footer-info{height:244px;background:var(--navy-deep);text-align:center;color:var(--footer-text)}
.footer-brand{position:absolute;top:40px;left:0;width:100%;display:flex;justify-content:center;align-items:center;gap:10px;color:var(--white);font-family:"Lato",sans-serif;font-weight:700;font-size:22px}
.footer-brand .dot{width:20px;height:20px;border-radius:50%;background:var(--white)}
.footer-address{position:absolute;top:100px;left:0;width:100%;font-size:12px;line-height:1.9}
.copyright{position:absolute;bottom:22px;left:0;width:100%;font-family:"Lato",sans-serif;font-size:10px;letter-spacing:1px;color:#6c7d92}
</style>
</head>
<body>

<header class="section hero">
  <div class="photo" role="img" aria-label="オフィスでノートパソコンを囲み談笑するスタッフの写真"></div>
  <div class="shade"></div>
  <div class="brand"><span class="dot"></span>Kano Mirea</div>
  <nav class="gnav">
    <a class="current" href="#">HOME</a>
    <a href="#">NEWS</a>
    <a href="#">COMPANY</a>
    <a href="#">BUSINESS</a>
    <a href="#">RECRUIT</a>
    <a href="#">CONTACT</a>
  </nav>
  <h1 class="hero-title">Discover the World!</h1>
</header>

<section class="section news">
  <h2 class="news-label">NEWS</h2>
  <div class="news-list">
    <article class="news-card">
      <div class="thumb" role="img" aria-label="新着情報のイメージ写真"></div>
      <div class="news-body">
        <p class="news-date">2017.08.01</p>
        <p class="news-text">当Webサイトをリニューアルしました。今後ともよろしくお願い致します。</p>
        <p class="news-more"><span>READ MORE</span><span>›</span></p>
      </div>
    </article>
    <article class="news-card">
      <div class="thumb" role="img" aria-label="新着情報のイメージ写真"></div>
      <div class="news-body">
        <p class="news-date">2017.08.01</p>
        <p class="news-text">当Webサイトをリニューアルしました。今後ともよろしくお願い致します。</p>
        <p class="news-more"><span>READ MORE</span><span>›</span></p>
      </div>
    </article>
    <article class="news-card">
      <div class="thumb" role="img" aria-label="新着情報のイメージ写真"></div>
      <div class="news-body">
        <p class="news-date">2017.08.01</p>
        <p class="news-text">当Webサイトをリニューアルしました。今後ともよろしくお願い致します。</p>
        <p class="news-more"><span>READ MORE</span><span>›</span></p>
      </div>
    </article>
    <article class="news-card">
      <div class="thumb" role="img" aria-label="新着情報のイメージ写真"></div>
      <div class="news-body">
        <p class="news-date">2017.08.01</p>
        <p class="news-text">当Webサイトをリニューアルしました。今後ともよろしくお願い致します。</p>
        <p class="news-more"><span>READ MORE</span><span>›</span></p>
      </div>
    </article>
  </div>
</section>

<section class="section feature business">
  <div class="photo" role="img" aria-label="地図アプリを表示したタブレットを操作する手元の写真"></div>
  <div class="shade"></div>
  <div class="feature-copy">
    <h2 class="feature-title">BUSINESS</h2>
    <p class="feature-lead">KanoMireaはインターネットを軸とした事業を展開しております。</p>
    <ul class="feature-items">
      <li>Internet media</li>
      <li>Promotion</li>
      <li>Influencer Marketing</li>
    </ul>
    <a class="btn" href="#">READ MORE <span>›</span></a>
  </div>
</section>

<section class="section feature recruit">
  <div class="photo" role="img" aria-label="オフィスで笑顔で話し合う社員の写真"></div>
  <div class="shade"></div>
  <div class="feature-copy">
    <h2 class="feature-title">RECRUIT</h2>
    <p class="feature-lead">KanoMireaの福利厚生や、<br>メンバーの1日の勤務スケジュールを公開</p>
    <ul class="feature-items">
      <li>Staff Interview</li>
      <li>One Day</li>
      <li>Blog</li>
    </ul>
    <a class="btn" href="#">READ MORE <span>›</span></a>
  </div>
</section>

<section class="section feature company">
  <div class="photo" role="img" aria-label="社名サインのある明るいオフィス受付の写真"></div>
  <div class="shade"></div>
  <div class="feature-copy">
    <h2 class="feature-title">COMPANY</h2>
    <p class="feature-lead">会社概要・沿革・代表挨拶</p>
    <ul class="feature-items">
      <li>overview</li>
      <li>history</li>
      <li>Greeting</li>
    </ul>
    <a class="btn" href="#">READ MORE <span>›</span></a>
  </div>
</section>

<footer>
  <nav class="section site-map">
    <div class="site-map-cols">
      <div class="site-map-col">
        <h3>Company（会社概要）</h3>
        <ul><li>会社概要</li><li>沿革</li><li>代表挨拶</li></ul>
      </div>
      <div class="site-map-col">
        <h3>Business（事業紹介）</h3>
        <ul><li>事業紹介</li></ul>
      </div>
      <div class="site-map-col">
        <h3>Recruit（採用情報）</h3>
        <ul><li>スタッフインタビュー</li><li>スタッフの1日</li><li>スタッフブログ</li></ul>
      </div>
      <div class="site-map-col">
        <h3>Contact（お問合せ）</h3>
        <ul><li>お問合せフォーム</li></ul>
      </div>
      <div class="site-map-col">
        <h3>News（新着情報）</h3>
        <ul><li>2017</li><li>2016</li></ul>
      </div>
    </div>
  </nav>
  <div class="section footer-info">
    <div class="footer-brand"><span class="dot"></span>Kano Mirea</div>
    <p class="footer-address">株式会社Kano Mirea（カノミレア）<br>〒150-0000　東京都渋谷区架空町1-2-3 サンプルビル5F　TEL 03-0000-0000</p>
    <p class="copyright">COPYRIGHT © KANO MIREA ALL RIGHTS RESERVED.</p>
  </div>
</footer>

</body>
</html>
```